New tech executive consulting company needs professionally branded document templates

We are a new business selling fractional board advisory and go-to-market consulting services into the Technology space. Partwise Helm are experts in providing high-quality executive-level leaders on a part-time basis to tech companies in need of their expertise. We work closely with clients to understand their business needs, challenges, and goals, and provides customised solutions to help them succeed. Due to our audience we need the design to have a high quality, executive look and feel.

Our first website is live and can be found at partwisehelm.tech. We also already have a logo which I've uploaded. Our brand is clean and uses orange to give it colour and an identity that stands out.

We need some document master templates created so we can create our own presentations (Google Slides & Powerpoint), PDF documents, and Word templates, and ideally also a LinkedIn banner.

```html
<!DOCTYPE html>
<html lang="en">
<head>
<meta charset="utf-8">
<title>Partwise Helm – Presentation Templates</title>
<link href="https://fonts.googleapis.com/css2?family=IBM+Plex+Sans:wght@300;400;600;700&display=swap" rel="stylesheet">
<style>
  :root{
    --orange:#ee8548;
    --ink:#2d333d;
    --body:#4a4f57;
    --page:#e6e7e9;
    --white:#ffffff;
    --slate:#5e6777;
    --photo-office:linear-gradient(135deg,#b9c6c9,#7e8f8c 55%,#4e5a5c);
    --photo-room:linear-gradient(135deg,#cfd6da,#93a0a6 50%,#58636a);
    --photo-portrait:linear-gradient(160deg,#6b5a3e,#3a4f72 60%,#22304b);
    --photo-sunset:linear-gradient(120deg,#f0d49a,#b58a55 45%,#3d3440);
  }
  *{box-sizing:border-box;margin:0;padding:0}
  html,body{width:1200px;height:3810px;overflow:hidden;background:var(--page);font-family:"IBM Plex Sans",Arial,sans-serif;color:var(--ink)}
  .slide{position:absolute;left:102px;width:1002px;height:564px;background:var(--white);overflow:hidden}
  .s1{top:90px}.s2{top:698px}.s3{top:1307px}.s4{top:1915px}.s5{top:2523px}.s6{top:3131px;background:var(--slate)}
  .abs{position:absolute}
  .photo{position:absolute}
  .brand{position:absolute;font-weight:700;color:var(--ink);letter-spacing:2px;line-height:1.05;text-transform:uppercase}
  .brand span{display:block}
  .brand span + span{text-align:right}
  .headline{position:absolute;font-weight:700;text-transform:uppercase;letter-spacing:.5px}
  .accent{color:var(--orange)}
  .copy{position:absolute;font-size:14.5px;line-height:22px;color:var(--body);font-weight:400}
  .copy p + p{margin-top:22px}
  .tag{position:absolute;background:var(--orange);color:var(--white);font-weight:700;font-size:34px;padding:0 4px;line-height:38px}
  .service{position:absolute;left:0;width:560px}
  .service .icon{position:absolute;left:31px;top:0;width:80px;height:80px;border-radius:50%;background:var(--orange)}
  .service h3{position:absolute;left:133px;top:0;font-size:14px;font-weight:700;letter-spacing:.5px}
  .service p{position:absolute;left:133px;top:22px;width:400px;font-size:14.5px;line-height:22px;color:var(--body)}
</style>
</head>
<body>

<!-- Cover -->
<section class="slide s1">
  <div class="photo" role="img" aria-label="Photo: smiling executive presenting at a boardroom table" style="inset:0;background:var(--photo-office);clip-path:polygon(478px 0,1002px 0,1002px 564px,396px 564px)"></div>
  <svg class="abs" width="1002" height="564" style="left:0;top:0"><polygon points="467,0 479,0 397,564 385,564" fill="var(--orange)"/></svg>
  <div class="brand" style="left:58px;top:48px;font-size:40px"><span>Partwise</span><span>Helm</span></div>
  <h1 class="headline" style="left:76px;top:222px;font-size:36px;line-height:50px">Experts in<br>providing<br><span class="accent">Executive<br>Leadership</span><br>on demand</h1>
</section>

<!-- About -->
<section class="slide s2">
  <div class="photo" role="img" aria-label="Photo: leader addressing a seated team in a bright office" style="inset:0;background:var(--photo-room);clip-path:polygon(470px 0,1002px 0,1002px 263px,434px 263px)"></div>
  <svg class="abs" width="1002" height="564" style="left:0;top:0"><polygon points="460,0 470,0 393,564 383,564" fill="var(--orange)"/></svg>
  <div class="brand" style="left:44px;top:64px;font-size:34px"><span>Partwise</span><span>Helm</span></div>
  <div class="tag" style="left:49px;top:237px">ABOUT</div>
  <h2 class="headline" style="left:44px;top:300px;font-size:38px;line-height:53px">The smart way<br>to scale your<br>business</h2>
  <div class="copy" style="left:475px;top:291px;width:490px">
    <p>Partwise Helm are experts in providing high-quality executive-level leaders on a part-time basis to tech companies in need of their expertise. We work closely with clients to understand their business needs, challenges, and goals, and provides customised solutions to help them succeed.</p>
    <p>Our strategic insights, leadership, and collaborative approach make us a valuable partner for companies looking to drive growth and innovation. We are passionate about helping companies achieve their goals and are committed to providing the highest level of service to our clients.</p>
  </div>
</section>

<!-- Founder -->
<section class="slide s3">
  <svg class="abs" width="1002" height="564" style="left:0;top:0">
    <polygon points="453,0 1002,0 1002,263 429,263" fill="var(--orange)"/>
    <polygon points="430,263 440,263 393,564 383,564" fill="var(--orange)"/>
  </svg>
  <div class="brand" style="left:39px;top:32px;font-size:30px"><span>Partwise</span><span>Helm</span></div>
  <div class="photo" role="img" aria-label="Portrait photo of the founder in a blue blazer" style="left:31px;top:127px;width:370px;height:416px;background:var(--photo-portrait)"></div>
  <h2 class="headline abs" style="left:480px;top:106px;width:444px;text-align:center;font-size:40px;color:var(--white)">Tom Carver</h2>
  <div class="copy" style="left:474px;top:311px;width:490px">
    <p>Tom Carver is a highly accomplished business leader with extensive experience in executive-level leadership and strategy. As the founder of Partwise Helm, Tom brings his years of experience in the technology industry to help companies achieve their goals.</p>
    <p>Throughout his career, Tom has held executive positions in companies ranging from startups to large corporations. He has a deep understanding of the tech industry and has helped companies at all stages of maturity drive significant growth and innovation.</p>
  </div>
</section>

<!-- Services -->
<section class="slide s4">
  <div class="photo" role="img" aria-label="Photo: consultant leading a discussion with colleagues around a table" style="inset:0;background:var(--photo-room);clip-path:polygon(644px 0,1002px 0,1002px 564px,563px 564px)"></div>
  <svg class="abs" width="1002" height="564" style="left:0;top:0">
    <polygon points="634,0 644,0 563,564 553,564" fill="var(--orange)"/>
    <line x1="253" y1="22" x2="237" y2="92" stroke="var(--orange)" stroke-width="2"/>
  </svg>
  <div class="brand" style="left:24px;top:20px;font-size:28px"><span>Partwise</span><span>Helm</span></div>
  <h2 class="headline" style="left:274px;top:34px;font-size:30px">Services</h2>
  <div class="service" style="top:139px">
    <div class="icon"></div>
    <h3>HEADING</h3>
    <p>Lorem ipsum dolor sit amet, consectetur adipiscing elit, sed do eiusmod tempor incididunt ut labore et dolore magna aliqua. Ut enim ad minim veniam, quis nostrud exercitation ullamco laboris nisi ut aliquip</p>
  </div>
  <div class="service" style="top:287px">
    <div class="icon"></div>
    <h3>HEADING</h3>
    <p>Lorem ipsum dolor sit amet, consectetur adipiscing elit, sed do eiusmod tempor incididunt ut labore et dolore magna aliqua. Ut enim ad minim veniam, quis nostrud exercitation ullamco laboris nisi ut aliquip</p>
  </div>
  <div class="service" style="top:432px">
    <div class="icon"></div>
    <h3>HEADING</h3>
    <p>Lorem ipsum dolor sit amet, consectetur adipiscing elit, sed do eiusmod tempor incididunt ut labore et dolore magna aliqua. Ut enim ad minim veniam, quis nostrud exercitation ullamco laboris nisi ut aliquip</p>
  </div>
</section>

<!-- Call to action -->
<section class="slide s5">
  <div class="photo" role="img" aria-label="Photo: speaker raising a fist before an applauding audience at sunset" style="inset:0;background:var(--photo-sunset);clip-path:polygon(930px 0,1002px 0,1002px 564px,0 564px,0 440px)"></div>
  <div class="brand" style="left:42px;top:40px;font-size:30px"><span>Partwise</span><span>Helm</span></div>
  <h2 class="headline" style="left:37px;top:120px;font-size:27px;line-height:33px">Let us help you take<br>your business to<br>the next level.<br><span class="accent">Contact us for a free<br>consultation.</span></h2>
</section>

<!-- Closing -->
<section class="slide s6" role="img" aria-label="Faint background photo of a meeting under a slate tint">
  <div class="brand" style="left:356px;top:96px;font-size:44px;color:var(--ink)"><span>Partwise</span><span>Helm</span></div>
  <svg class="abs" width="1002" height="564" style="left:0;top:0">
    <line x1="349" y1="263" x2="648" y2="263" stroke="var(--white)" stroke-width="2"/>
    <line x1="349" y1="365" x2="648" y2="365" stroke="var(--white)" stroke-width="2"/>
  </svg>
  <div class="abs" style="left:300px;top:274px;width:400px;text-align:center;font-size:62px;font-weight:300;color:var(--white)">Thank You</div>
  <div class="abs" style="left:0;top:486px;width:1002px;text-align:center;font-size:15px;color:var(--white)">info@partwisehelm.tech &nbsp;&nbsp; | &nbsp;&nbsp; +44 7700 900123 &nbsp;&nbsp; | &nbsp;&nbsp; Tom Carver</div>
</section>

</body>
</html>
```